Packaging Design Project for a Pet Product Company

Need a packaging design for a pet product company based in Los Angeles. We offer user-friendly pet products to people. This new product is a Collapsible Pet Bowl that folds in 4 ways for dogs of all sizes. It can be used for food or water. It is light-weight, functional and eco-friendly. Great for indoor/outdoor use at home and it's easy to take on the go.

www.tuftmeadow.com - get the look and feel of our design.
(This project is for a new bowl which is not yet announced on our website.)

I can be reached via the SketchHive comment board or at rilo481@mailvendo.com.

Target Market(s)

Pet boutique owners and customers

Industry/Entity Type

It Company

Requirements
Must have
• Use kraft paper as the background color of the design

Maintain a Modern, fun, creative and eco-friendly look in the design

color scheme:
Background color: kraft paper
Design & Font color: WHITE and CHARCOAL GREY are must. Possibly a 3rd color (Tuft Meadow logo green or any 3rd color of your choice)

Maintain consistency with our "existing packaging for current product line" (see attached file)

Picture of a Labradoodle dog with a bowl in front of the dog (black and white)
Nice to have
• Play around with the composition/layout of the design and suggest any creative touch to make it better

Modify the wording/content if necessary

Mock-up rendering should be as realistic as possible

Use one of our bowl color in mock-up rendering. Same packaging for pink bowl and the green bowl.

```html
<!DOCTYPE html>
<html lang="en">
<head>
<meta charset="utf-8">
<title>Tuft Meadow – Collapsible Pet Bowl Packaging</title>
<link rel="stylesheet" href="https://fonts.googleapis.com/css2?family=Chewy&family=Patrick+Hand&display=swap">
<style>
  :root {
    --backdrop: #ece8e2;
    --kraft: #9b6a3c;
    --kraft-dark: #8a5c32;
    --leaf-green: #b5d412;
    --charcoal: #2f2a26;
    --white: #ffffff;
    --slot: #3a2a1e;
  }
  html, body {
    margin: 0;
    width: 1200px;
    height: 815px;
    overflow: hidden;
    background: var(--backdrop);
  }
  .stage {
    position: relative;
    width: 1122px;
    height: 762px;
    transform: scale(1.0695);
    transform-origin: 0 0;
    font-family: "Patrick Hand", cursive;
  }
  .kraft {
    position: absolute;
    background: repeating-linear-gradient(90deg, var(--kraft) 0 3px, var(--kraft-dark) 3px 4px);
  }
  .band {
    position: absolute;
    background: var(--leaf-green);
  }
  .hang-slot {
    position: absolute;
    height: 12px;
    background: var(--slot);
    border-radius: 6px;
  }
  .brand {
    position: absolute;
    display: flex;
    align-items: center;
    gap: 6px;
    color: var(--leaf-green);
    font-size: 17px;
    white-space: nowrap;
  }
  .brand-mark {
    width: 12px;
    height: 12px;
    background: var(--leaf-green);
  }

  /* Front panel */
  .front-badge {
    left: 78px; top: 245px; width: 412px; height: 400px;
    border-radius: 50%;
  }
  .front-title {
    position: absolute;
    left: 150px; top: 212px; width: 260px;
    margin: 0;
    font-family: "Chewy", cursive;
    font-weight: 400;
    font-size: 46px;
    line-height: 44px;
    color: var(--charcoal);
    text-align: center;
    transform: rotate(-7deg);
  }
  .front-art {
    position: absolute;
    left: 128px; top: 315px; width: 300px; height: 325px;
    border-radius: 50%;
    background: radial-gradient(circle at 55% 45%, rgba(181,212,18,0.55), rgba(181,212,18,0.25) 60%, rgba(181,212,18,0) 72%);
  }
  .front-specs {
    position: absolute;
    left: 147px; top: 670px; width: 189px;
    margin: 0;
    color: var(--white);
    font-size: 17px;
    line-height: 27px;
    text-align: center;
    white-space: nowrap;
  }
  .front-specs span { display: block; margin-left: -60px; margin-right: -60px; }

  /* Back panel */
  .feature-tag {
    position: absolute;
    left: 777px; top: 247px; width: 200px; height: 23px;
    background: var(--leaf-green);
    color: var(--charcoal);
    font-size: 16px;
    line-height: 23px;
    text-align: center;
  }
  .feature-list {
    position: absolute;
    left: 788px; top: 286px;
    margin: 0; padding: 0;
    list-style: none;
    color: var(--white);
    font-size: 15px;
    line-height: 17px;
  }
  .feature-list li { display: flex; align-items: center; gap: 6px; }
  .feature-list li::before {
    content: "";
    width: 8px; height: 8px;
    border-radius: 50%;
    background: var(--leaf-green);
  }
  .tagline {
    position: absolute;
    left: 760px; top: 345px; width: 220px;
    margin: 0;
    color: var(--white);
    font-size: 17px;
    line-height: 20px;
    text-align: center;
    transform: rotate(-4deg);
  }
  .benefits, .materials, .site-url {
    position: absolute;
    left: 737px; width: 260px;
    margin: 0;
    color: var(--charcoal);
    font-size: 15px;
    line-height: 16px;
    text-align: center;
  }
  .benefits { top: 403px; }
  .materials { top: 533px; }
  .site-url { top: 593px; }
  .care-icons {
    position: absolute;
    left: 793px; top: 494px;
    display: flex; gap: 8px;
  }
  .care-icons span {
    width: 28px; height: 28px;
    border-radius: 50%;
    border: 2px solid var(--white);
    box-sizing: border-box;
  }
</style>
</head>
<body>
<main class="stage">

  <!-- Front panel -->
  <section class="front" aria-label="Front of package">
    <div class="kraft" style="left:157px;top:5px;width:170px;height:165px;"></div>
    <div class="hang-slot" style="left:232px;top:40px;width:24px;"></div>
    <div class="brand" style="left:196px;top:112px;"><span class="brand-mark"></span>Tuft Meadow</div>
    <div class="band" style="left:147px;top:165px;width:189px;height:20px;"></div>
    <div class="kraft" style="left:147px;top:185px;width:189px;height:572px;"></div>
    <div class="kraft front-badge"></div>
    <h1 class="front-title">Collapsible<br>Pet bowl</h1>
    <div class="front-art" role="img" aria-label="Green leaf swirl around a drawing of a collapsible bowl"></div>
    <p class="front-specs">
      <span>100% Silicone</span>
      <span>64 oz. / 8 cups Capacity</span>
      <span>Fold down to only 1.5 inches</span>
    </p>
  </section>

  <!-- Back panel -->
  <section class="back" aria-label="Back of package">
    <div class="kraft" style="left:737px;top:10px;width:236px;height:190px;"></div>
    <div class="hang-slot" style="left:818px;top:40px;width:72px;height:14px;"></div>
    <div class="brand" style="left:818px;top:152px;"><span class="brand-mark"></span>Tuft Meadow</div>
    <div class="band" style="left:737px;top:200px;width:260px;height:18px;"></div>
    <div class="kraft" style="left:737px;top:218px;width:260px;height:530px;"></div>

    <div class="feature-tag">Adjustable to 4 different sizes</div>
    <ul class="feature-list">
      <li>it's like having 4 bowls in one!</li>
      <li>Easy to clean</li>
      <li>Non-slip design</li>
    </ul>
    <p class="tagline">Lightweight, Functional<br>and Eco-friendly</p>
    <p class="benefits">
      For dogs of all sizes<br>
      No splattered mess<br>
      Use for food or water<br>
      Great for indoor/outdoor use at<br>
      home and easy to take on the go
    </p>
    <div class="care-icons" aria-hidden="true">
      <span></span><span></span><span></span><span></span>
    </div>
    <p class="materials">
      100% Food Grade Silicone<br>
      Dishwasher Safe (Top Rack)<br>
      FDA Food-Safe Silicone
    </p>
    <p class="site-url">www.tuftmeadow.com</p>
  </section>

</main>
</body>
</html>
```